Mortgage Protection Insurance Flyer

The target audience are new home owners so the design needs to be clean and simple.

This a primarily for Final Expense Insurance, but need an area where it says "We Also Specialize In:"
- Medicare Supplement Insurance (MediGap)
- Annuities
- Final Expense

All flyer versions need to be editable. Colors to be used are red, white or black. Refer to my website for colors and photos (harborvaleassurance.com). Will attach my logo and a flyer that I found online that is the format that I am looking for (for 8.5 in. x 11 in version). Need flyer in standard letter size 8.5 in. x11 in. but also in 8.5 in. x 5.5 in and 5.0 in. x 8.0 in. All sizes to be portrait oriented. If picked as winning design, need all flyer versions in full color, also in grey scale and files in all industry file types.

Content can be taken from my website..... harborvaleassurance.com

Do NOT submit if you are not willing to provide all versions as described above for the original project price.

Must use royalty-free stock photos please.

Target Market(s)

New homeowners looking for insurance to protect there mortgage payments

Industry/Entity Type

Life Insurance

Colors
f69fa3

Requirements
Must have
• Colors to be used are red, white or black.
• Need flyer in standard letter size 8.5 in. x11 in. but also in 3.5 in. x 8.5 in (Full Bleed 3.75 in by 8.75 in.) and 4.0 in. x 6.0 in. (Full Bleed 4.12 in x 6.12 in) Each design tailored to the size dimensions (So no squeezing 8.5 x 11 design into a 4.0 x 6.0 space.) All sizes to be portrait oriented. If picked as winning design, need all flyer versions in full color, also in grey scale and files in all file types.
• Do not need physical address on flyer, do need email address on flyer though - tkerlow@harborvaleassurance.com
• So phone number should be prominent, email address and website address should also be contact area.
• If you can not agree to terms above, do not submit any designs.
• Need facebook & twitter logos somewhere in contact info area.
Nice to have
• See sample flyers I have attached.
• White background with red used as primary graphic color and black used as secondary graphic if needed.
• font to be used should similar to one used in logo.

```html
<!DOCTYPE html>
<html lang="en">
<head>
<meta charset="utf-8">
<title>Harborvale Assurance – Flyer</title>
<link href="https://fonts.googleapis.com/css2?family=Anton&family=Lato:wght@400;700;900&display=swap" rel="stylesheet">
<style>
  :root{
    --red:#e0141b;
    --red-deep:#b10d12;
    --black:#1c1c1c;
    --ink:#2b2b2b;
    --white:#ffffff;
    --stage:#e9e9e9;
    --photo-light:#f1e3cf;
    --photo-mid:#d9b88f;
    --photo-warm:#b98a5c;
  }
  *{box-sizing:border-box;margin:0;padding:0}
  html,body{width:1200px;height:1200px;overflow:hidden;background:var(--stage)}
  body{font-family:"Lato",Arial,sans-serif;color:var(--ink)}
  .flyer{position:absolute;left:160px;top:30px;width:880px;height:1140px;background:var(--white);overflow:hidden;box-shadow:0 6px 24px rgba(0,0,0,.18)}
  .flyer svg.shape{position:absolute;left:0;top:0}

  .brand{position:absolute;left:40px;top:62px;display:flex;align-items:center;gap:9px;font-weight:900;font-size:22px;letter-spacing:.5px;line-height:1;color:var(--black);text-transform:uppercase}
  .brand-dot{width:12px;height:12px;border-radius:50%;background:var(--red)}

  .headline{position:absolute;left:62px;top:262px;font-family:"Anton",Impact,sans-serif;font-weight:400;text-transform:uppercase;line-height:1}
  .headline .l1{font-size:62px;color:var(--black)}
  .headline .l2{font-size:62px;color:var(--red)}
  .headline .l3{font-size:38px;color:var(--black);margin-top:4px}

  .intro{position:absolute;left:48px;top:505px;width:430px;font-size:19px;line-height:1.3;color:var(--ink)}

  .section{position:absolute;width:440px}
  .section h2{color:var(--red);font-weight:900;font-size:20px;line-height:1.2;margin-bottom:8px}
  .section p{font-size:13px;line-height:1.4;margin-bottom:8px}
  .section p:last-child{margin-bottom:0}
  .final-expense{left:48px;top:596px}
  .about{left:48px;top:700px}
  .medigap{left:500px;top:705px;width:345px}
  .medigap h2,.specialties h2{font-size:16px}
  .specialties{left:500px;top:822px;width:345px}
  .specialties ul{list-style:none}
  .specialties li{display:flex;align-items:center;gap:8px;font-size:13px;line-height:20px}
  .specialties li::before{content:"";width:6px;height:6px;border-radius:50%;background:var(--red);flex:none}

  .benefits{position:absolute;left:498px;top:440px;width:350px;height:235px;border-radius:38px;background:linear-gradient(160deg,var(--red) 0%,var(--red-deep) 100%);padding:62px 26px 18px 30px;color:var(--white)}
  .benefits-tag{position:absolute;left:-14px;top:20px;background:var(--black);color:var(--white);font-weight:900;font-size:22px;padding:6px 22px 6px 18px;border-radius:0 18px 18px 0}
  .benefits ul{list-style:none}
  .benefits li{display:flex;gap:10px;font-size:13.5px;line-height:1.3;margin-bottom:7px}
  .benefits li svg{flex:none;margin-top:1px}

  .call{position:absolute;left:48px;top:1018px;color:var(--white)}
  .call .label{font-weight:900;font-size:30px;line-height:1.2}
  .call .phone{font-weight:900;font-size:50px;letter-spacing:1px;line-height:1.05}

  .contact-list{position:absolute;left:470px;top:985px;display:flex;flex-direction:column;gap:6px}
  .contact-line{display:flex;align-items:center;gap:10px;color:var(--white);font-weight:700;font-size:14px;line-height:1}
  .icon-ring{width:30px;height:30px;border:2px solid var(--white);border-radius:50%;display:flex;align-items:center;justify-content:center;flex:none}
  .social{display:flex;gap:10px;margin-top:2px}
  .social-spot{width:28px;height:28px;border-radius:50%;background:var(--white)}
</style>
</head>
<body>
<main class="flyer">
  <svg class="shape" width="880" height="1140" viewBox="0 0 880 1140" role="img" aria-label="Photograph of a smiling family sitting on a wooden floor under a cardboard roof shape">
    <defs>
      <linearGradient id="photoTone" x1="0" y1="0" x2="1" y2="1">
        <stop offset="0" stop-color="var(--photo-light)"/>
        <stop offset=".55" stop-color="var(--photo-mid)"/>
        <stop offset="1" stop-color="var(--photo-warm)"/>
      </linearGradient>
    </defs>
    <path d="M0 250 C200 220 420 120 520 0 L880 0 L880 400 C700 440 300 500 0 470 Z" fill="url(#photoTone)"/>
  </svg>
  <svg class="shape" width="880" height="1140" viewBox="0 0 880 1140" aria-hidden="true">
    <defs>
      <linearGradient id="bandTone" x1="0" y1="0" x2="0" y2="1">
        <stop offset="0" stop-color="var(--red)"/>
        <stop offset="1" stop-color="var(--red-deep)"/>
      </linearGradient>
    </defs>
    <path d="M0 250 C200 220 420 120 520 0" fill="none" stroke="var(--red)" stroke-width="6"/>
    <path d="M0 240 C200 210 410 112 505 0" fill="none" stroke="var(--black)" stroke-width="4"/>
    <path d="M0 470 C300 500 700 440 880 400" fill="none" stroke="var(--red)" stroke-width="6"/>
    <path d="M0 486 C300 516 700 456 880 414" fill="none" stroke="var(--black)" stroke-width="7"/>
    <path d="M0 986 C300 961 600 946 880 906" fill="none" stroke="var(--black)" stroke-width="5"/>
    <path d="M0 1000 C300 975 600 960 880 920 L880 1140 L0 1140 Z" fill="url(#bandTone)"/>
  </svg>

  <div class="brand"><span class="brand-dot"></span>Harborvale Assurance</div>

  <h1 class="headline">
    <div class="l1">Our</div>
    <div class="l2">Plans are</div>
    <div class="l3">Based on yours</div>
  </h1>

  <p class="intro">Get the right Final Expense Insurance, Medicare Supplement Insurance or Mortgage Protection Insurance plan for your family's peace-of-mind!</p>

  <section class="section final-expense">
    <h2>Final Expense Insurance</h2>
    <p>Final Expense Insurance is a type of permanent life insurance where the death benefit is used to cover (but not limited to) medical costs, funeral costs and other end-of-life expenses. It is a budget friendly option with a death benefit of up to $35k.</p>
  </section>

  <section class="section about">
    <h2>About Us</h2>
    <p>Unforeseen events and a lack of the right kind of insurance can spell trouble quickly. Contact us today, to set up a free assessment time. We will analyze your insurance needs and get you and your family the right coverage quickly at a budget friendly price. Everyone has different insurance needs.</p>
    <p>Find out how we can give you the peace of mind knowing your family wont have a financial burden if something were to happen to you.</p>
    <p>Find out how we can help find the right plan to keep your medical costs manageable.</p>
  </section>

  <aside class="benefits">
    <div class="benefits-tag">Benefits:</div>
    <ul>
      <li><svg width="16" height="16" viewBox="0 0 16 16"><circle cx="8" cy="8" r="7" fill="none" stroke="#fff" stroke-width="1.5"/><path d="M4.5 8.2 L7 10.5 L11.5 5.8" fill="none" stroke="#fff" stroke-width="1.6"/></svg>Relatively low monthly premiums</li>
      <li><svg width="16" height="16" viewBox="0 0 16 16"><circle cx="8" cy="8" r="7" fill="none" stroke="#fff" stroke-width="1.5"/><path d="M4.5 8.2 L7 10.5 L11.5 5.8" fill="none" stroke="#fff" stroke-width="1.6"/></svg>Premiums can never increase</li>
      <li><svg width="16" height="16" viewBox="0 0 16 16"><circle cx="8" cy="8" r="7" fill="none" stroke="#fff" stroke-width="1.5"/><path d="M4.5 8.2 L7 10.5 L11.5 5.8" fill="none" stroke="#fff" stroke-width="1.6"/></svg>Your policy can never be cancelled as long as you pay your premium</li>
      <li><svg width="16" height="16" viewBox="0 0 16 16"><circle cx="8" cy="8" r="7" fill="none" stroke="#fff" stroke-width="1.5"/><path d="M4.5 8.2 L7 10.5 L11.5 5.8" fill="none" stroke="#fff" stroke-width="1.6"/></svg>No medical exams</li>
      <li><svg width="16" height="16" viewBox="0 0 16 16"><circle cx="8" cy="8" r="7" fill="none" stroke="#fff" stroke-width="1.5"/><path d="M4.5 8.2 L7 10.5 L11.5 5.8" fill="none" stroke="#fff" stroke-width="1.6"/></svg>Guaranteed Death Benefit</li>
      <li><svg width="16" height="16" viewBox="0 0 16 16"><circle cx="8" cy="8" r="7" fill="none" stroke="#fff" stroke-width="1.5"/><path d="M4.5 8.2 L7 10.5 L11.5 5.8" fill="none" stroke="#fff" stroke-width="1.6"/></svg>Many policies are Guaranteed Acceptance</li>
    </ul>
  </aside>

  <section class="section medigap">
    <h2>Medicare Supplement Insurance (MediGap)</h2>
    <p>Medicare Supplement Insurance (also called MediGap) helps pay the “gap” between what Original Medicare (Medicare Parts A and B) pays and what you pay out of your own pocket.</p>
  </section>

  <section class="section specialties">
    <h2>We Also Specialize In:</h2>
    <ul>
      <li>Medicare Supplement Insurance (MediGap)</li>
      <li>Annuities</li>
      <li>Final Expense</li>
    </ul>
  </section>

  <div class="call">
    <div class="label">Call us now:</div>
    <div class="phone">(208)555.0147</div>
  </div>

  <div class="contact-list">
    <div class="contact-line">
      <span class="icon-ring"><svg width="14" height="18" viewBox="0 0 14 18"><path d="M7 17 C3 11 1 8.5 1 6 A6 6 0 0 1 13 6 C13 8.5 11 11 7 17 Z" fill="#fff"/><circle cx="7" cy="6" r="2.2" fill="var(--red)"/></svg></span>
      harborvaleassurance.com
    </div>
    <div class="contact-line">
      <span class="icon-ring"><svg width="16" height="12" viewBox="0 0 18 14"><rect x="1" y="1" width="16" height="12" fill="none" stroke="#fff" stroke-width="1.8"/><path d="M1 1 L9 8 L17 1" fill="none" stroke="#fff" stroke-width="1.8"/></svg></span>
      tkerlow@harborvaleassurance.com
    </div>
    <div class="contact-line">
      <span class="icon-ring"><svg width="14" height="14" viewBox="0 0 14 14"><path d="M1 7 L7 1.5 L13 7 M3 6 V13 H11 V6" fill="none" stroke="#fff" stroke-width="1.8"/></svg></span>
      PO Box 412 Cedar Hollow, Idaho, United States
    </div>
    <div class="social" aria-label="Social media links">
      <span class="social-spot"></span>
      <span class="social-spot"></span>
    </div>
  </div>
</main>
</body>
</html>
```